Business card design needed

We need a new business card design to re launch my carpentry business. Could include double sided card with list of services provided.
Kitchens, bathrooms, decks, pergolas, window replacements, timber floor installation, owner builder assistance and general carpentry.
Would like an eye catching card that becons to be read in bright colors that has a logo that could be also used on clothing vehicle sinage etc
Preferably in blues and reds we live near beach so maybe some type of Beecher feel
The target market of my business would be mainly individuals requiring professional carpentry services not just a handy man. The renovation market plays a big part of my business
Carpentry
Carpenter & joiner
Rob Halvorsen
Seabrook
marlo_petey@tidalnet.com
0428913560

```html
<!DOCTYPE html>
<html lang="en">
<head>
<meta charset="utf-8">
<title>Rob Halvorsen – Carpenter &amp; Joiner business card</title>
<link href="https://fonts.googleapis.com/css2?family=Cinzel:wght@400;600&family=Poiret+One&family=Kalam&family=Share+Tech+Mono&display=swap" rel="stylesheet">
<style>
  :root {
    --bg: #2b2b2d;
    --card-black: #0b0b0c;
    --card-charcoal: #1c1c1e;
    --teal: #16788f;
    --teal-soft: #2690a8;
    --white: #f4f4f4;
    --ink: #111;
    --service-text: #e6e6e6;
  }
  * { box-sizing: border-box; margin: 0; padding: 0; }
  html, body { width: 1200px; height: 900px; overflow: hidden; }
  body { background: var(--bg); position: relative; }

  .card {
    position: absolute;
    width: 600px;
    height: 343px;
    border-radius: 4px;
    overflow: hidden;
    box-shadow: 0 18px 40px rgba(0,0,0,.55);
  }
  .card svg.card-shapes { position: absolute; inset: 0; }

  /* Services side */
  .card-services { left: 110px; top: 80px; background: var(--card-black); }
  .photo-panel {
    position: absolute;
    left: 240px; top: 58px;
    width: 330px; height: 218px;
    background: linear-gradient(100deg, #6e5a44 0%, #b7a58a 25%, #8b8f86 45%, #c9b58e 70%, #e0c48f 100%);
    opacity: .9;
  }
  .service-list {
    position: absolute;
    left: 240px; top: 18px;
    width: 330px;
    font-family: "Cinzel", serif;
    color: var(--service-text);
    letter-spacing: 1.5px;
    text-shadow: 0 1px 3px rgba(0,0,0,.8);
  }
  .service-list li { list-style: none; font-size: 17px; line-height: 1; }
  .service-list .service-lead { height: 40px; font-size: 16px; }
  .service-list .service-strip { height: 54px; padding: 18px 0 0 14px; }
  .service-list .service-strip:nth-child(3) { padding-left: 60px; }
  .service-list .service-strip:nth-child(4) { padding-left: 36px; }
  .service-list .service-strip:nth-child(5) { padding-left: 20px; }
  .service-list .service-tail { padding-top: 22px; font-size: 15px; }

  /* Contact side */
  .card-contact { left: 490px; top: 470px; background: var(--card-black); }
  .contact-phone {
    position: absolute; left: 40px; top: 118px;
    font-family: "Share Tech Mono", monospace;
    font-size: 30px; letter-spacing: 3px; color: var(--ink);
  }
  .contact-email {
    position: absolute; left: 28px; top: 168px;
    font-family: "Kalam", cursive;
    font-size: 14px; color: var(--ink);
  }
  .brand {
    position: absolute; left: 395px; top: 32px;
    width: 180px; text-align: center;
  }
  .brand-mark {
    display: block; width: 78px; height: 78px; margin: 0 auto 8px;
    border-radius: 50%; background: var(--teal);
    border: 6px solid var(--white);
  }
  .brand-name {
    font-family: "Poiret One", sans-serif;
    font-size: 16px; letter-spacing: 2px; color: var(--white);
  }
  .trade {
    position: absolute; left: 380px; top: 170px; width: 210px;
    font-family: "Poiret One", sans-serif;
    color: var(--white); font-size: 22px; letter-spacing: 2px;
    text-transform: uppercase; line-height: 1.35;
  }
  .trade .initial { color: var(--teal-soft); font-size: 30px; }
  .trade .amp { display: block; text-align: center; }
  .trade .line-2 { display: block; text-align: center; }
  .owner-name {
    position: absolute; left: 360px; top: 282px; width: 225px; text-align: right;
    font-family: "Poiret One", sans-serif; text-transform: uppercase;
    font-size: 24px; letter-spacing: 2px; color: var(--teal-soft);
  }
</style>
</head>
<body>

<section class="card card-services" aria-label="Services side">
  <svg class="card-shapes" width="600" height="343" viewBox="0 0 600 343">
    <circle cx="-120" cy="360" r="330" fill="var(--teal)"/>
    <circle cx="-150" cy="370" r="322" fill="var(--card-charcoal)"/>
  </svg>
  <div class="photo-panel" role="img" aria-label="Strips of renovation photos: kitchen, bathroom, window and timber floor"></div>
  <ul class="service-list">
    <li class="service-lead">Owner Builder Assistance</li>
    <li class="service-strip">Kitchens</li>
    <li class="service-strip">Bathrooms</li>
    <li class="service-strip">Window Replacements</li>
    <li class="service-strip">Timber Floor Installations</li>
    <li class="service-tail">Decks • Pergolas • General Carpentry</li>
  </ul>
</section>

<section class="card card-contact" aria-label="Contact side">
  <svg class="card-shapes" width="600" height="343" viewBox="0 0 600 343">
    <circle cx="20" cy="330" r="345" fill="var(--teal)"/>
    <circle cx="10" cy="330" r="325" fill="var(--white)"/>
  </svg>
  <p class="contact-phone">0428913560</p>
  <p class="contact-email">Seabrook marlo_petey@tidalnet.com</p>
  <div class="brand">
    <span class="brand-mark"></span>
    <span class="brand-name">Halvorsen</span>
  </div>
  <p class="trade">
    <span class="line-1"><span class="initial">C</span>arpenter</span>
    <span class="amp">&amp;</span>
    <span class="line-2"><span class="initial">J</span>oiner</span>
  </p>
  <p class="owner-name">Rob Halvorsen</p>
</section>

</body>
</html>
```